A Freight forwarding (transportation/shipping) company requires stationary designs

We need The following:
1. Letterhead
2. Letter Envelope
3. Business Card Design
4. A4 Paper Envelope
5. A4 Paper Folder (One that is 2xA4 foldable size which we can open in half and we can put a paper in between and has a lot for business card)
6. A5 Paper (To be used for notes taking)
a design for a freight forwarding company named KORVELA MIND INTERNATIONAL TRANSPORTATION.
(We are active in Sea Transportation, Truck transportation, and Air Transportation, (printed design in PDF is required with all open source files for editing - lamination accepted)
Playing around with the Logo is accepted,, Korvela Logo.png is the correct logo.
Example of folder, envelopes, and notepad attached
Address of the company is :
No 7, 4th Tarandil Gharbi, Neshat Lar Blvd,
Mashhad, IR
Tel : +98 51 37412958
Fax : +98 51 37490316
Website : www.korvela-example.com
Email : info@korvela-example.com

```html
<!DOCTYPE html>
<html lang="en">
<head>
<meta charset="utf-8">
<title>Korvela Mind – Business Card</title>
<link href="https://fonts.googleapis.com/css2?family=Roboto+Condensed:wght@400;500&family=Roboto:wght@400&display=swap" rel="stylesheet">
<style>
  :root {
    --backdrop: #e4e4e4;
    --card-white: #f6f6f6;
    --brand-purple: #3d3a98;
    --brand-green: #3a9a3b;
    --text-grey: #555555;
    --divider: #9a9a9a;
    --white: #ffffff;
  }
  * { margin: 0; padding: 0; box-sizing: border-box; }
  html, body {
    width: 1200px; height: 960px; overflow: hidden;
    background: var(--backdrop);
    font-family: "Roboto", Arial, sans-serif;
  }
  .canvas { position: relative; width: 1200px; height: 960px; }

  .card { position: absolute; width: 600px; height: 343px; }
  .card-front { left: 314px; top: 113px; background: var(--card-white); }
  .card-back { left: 311px; top: 472px; background: var(--brand-purple); }

  .brand-mark { position: absolute; display: flex; flex-direction: column; align-items: center; }
  .card-front .brand-mark { left: 92px; top: 70px; width: 160px; }
  .card-back .brand-mark { left: 220px; top: 66px; width: 160px; }
  .brand-circle { width: 130px; height: 130px; border-radius: 50%; border: 10px solid var(--brand-purple); }
  .card-back .brand-circle { width: 150px; height: 150px; border-color: var(--white); }
  .brand-name {
    margin-top: 26px;
    font-family: "Roboto Condensed", Arial, sans-serif;
    font-weight: 400; font-size: 20px; letter-spacing: 0.2px;
    color: var(--brand-purple); white-space: nowrap;
  }
  .card-back .brand-name { margin-top: 6px; color: var(--white); }

  .divider { position: absolute; left: 297px; top: 72px; width: 2px; height: 203px; background: var(--divider); }

  .contact { position: absolute; left: 344px; top: 74px; color: var(--text-grey); }
  .person-name {
    font-family: "Roboto Condensed", Arial, sans-serif; font-weight: 500;
    font-size: 22px; color: var(--brand-purple); line-height: 26px;
  }
  .person-role {
    font-family: "Roboto Condensed", Arial, sans-serif; font-weight: 500;
    font-size: 16px; color: var(--brand-green); line-height: 22px;
  }
  .address { margin-top: 8px; font-size: 14.5px; line-height: 18px; }
  .contact-list { list-style: none; margin-top: 4px; font-size: 14.5px; }
  .contact-list li { display: flex; align-items: center; height: 19px; }
  .contact-list svg { width: 13px; height: 13px; margin-right: 10px; fill: var(--brand-purple); }

  .web-address {
    position: absolute; left: 0; right: 0; top: 296px; text-align: center;
    font-size: 14px; letter-spacing: 8px; color: var(--white);
  }
</style>
</head>
<body>
<main class="canvas">
  <section class="card card-front" aria-label="Business card front">
    <div class="brand-mark">
      <div class="brand-circle"></div>
      <div class="brand-name">KORVELA MIND</div>
    </div>
    <div class="divider"></div>
    <div class="contact">
      <h1 class="person-name">DAREN HOLM</h1>
      <p class="person-role">CEO/FOUNDER</p>
      <p class="address">No 7, 4th Tarandil Gharbi<br>Neshat Lar Blvd,<br>Mashhad, IR</p>
      <ul class="contact-list">
        <li><svg viewBox="0 0 16 16" aria-hidden="true"><path d="M3.5 1l3 3-1.6 2.2a9 9 0 0 0 4.9 4.9L12 9.5l3 3-1.6 2.2C7.5 14.5 1.5 8.5 1.3 2.6z"/></svg>+98 51 37412958</li>
        <li><svg viewBox="0 0 16 16" aria-hidden="true"><path d="M4 1h8v4H4zM1 6h14v6h-3v3H4v-3H1zm4 4v4h6v-4z"/></svg>+98 51 37490316</li>
        <li><svg viewBox="0 0 16 16" aria-hidden="true"><path d="M1 3h14v1.2L8 8.6 1 4.2zm0 2.6l7 4.4 7-4.4V13H1z"/></svg>info@korvela-example.com</li>
        <li><svg viewBox="0 0 16 16" aria-hidden="true"><path d="M8 1a7 7 0 1 0 0 14A7 7 0 0 0 8 1zm-1 2.2v2.3L5 7l1 2 1 .5V13A5 5 0 0 1 3.2 6.5zM9 13v-2l2-2-1-2H8V4l1-1a5 5 0 0 1 0 10z"/></svg>www.korvela-example.com</li>
      </ul>
    </div>
  </section>

  <section class="card card-back" aria-label="Business card back">
    <div class="brand-mark">
      <div class="brand-circle"></div>
      <div class="brand-name">KORVELA MIND</div>
    </div>
    <p class="web-address">www.korvela-example.com</p>
  </section>
</main>
</body>
</html>
```